Venture Capital Investment Firm

We are looking to overhaul our existing website (substantially), with only using the same logos (which we can provide).
We are an investment firm that focuses on making loans to late stage technology companies. Our site should ultimately look like other venture capital firms, and look modern and fresh. We have an existing website www.northvaleloan.com which this will be replacing, although we will be using a lot of the existing written content, and potentially the numbers of pages we will need, we are not wed to anything else. Please feel free to shoot any questions at any time and thank you in advance for your help!
Websites we like as examples:
https://www.tkbrandel.com/
https://www.emberwoodfunds.com/
Target Market(s)
Potential investors who will invest in our firm, as well as potentially companies that are looking to borrow money from us.

```html
<!DOCTYPE html>
<html lang="en">
<head>
<meta charset="utf-8">
<title>Northvale — Flexible Capital</title>
<link href="https://fonts.googleapis.com/css2?family=Cinzel:wght@600;700&family=Lato:wght@400;700&display=swap" rel="stylesheet">
<style>
:root{
  --navy:#1e4a74;
  --navy-deep:#173b60;
  --teal:#2a6677;
  --teal-soft:#6f9aa3;
  --orange:#f2693a;
  --ink:#1f3556;
  --text:#5d6470;
  --ghost:#d3dde6;
  --white:#ffffff;
}
*{margin:0;padding:0;box-sizing:border-box}
html,body{width:1200px;height:4501px;overflow:hidden}
body{position:relative;background:var(--white);font-family:'Lato',sans-serif;color:var(--text)}
.abs{position:absolute}
.serif{font-family:'Cinzel',serif;font-variant:small-caps}
a{color:inherit;text-decoration:none}

/* header & hero */
.hero{left:0;top:0;width:1200px;height:673px;background:linear-gradient(160deg,#234f7a,#1c4670)}
.brand{display:flex;align-items:center;gap:12px;color:var(--white);font-family:'Cinzel',serif;font-weight:700;font-size:34px}
.brand-dot{width:34px;height:34px;border-radius:50%;background:var(--white)}
.nav{display:flex;gap:24px;font-size:13px;color:var(--white)}
.phone-btn{width:37px;height:37px;background:#3f78b4;border-radius:3px;display:flex;align-items:center;justify-content:center}
.hero-title{color:var(--white);font-size:39px;line-height:52px;font-weight:600}
.btn{background:var(--orange);color:var(--white);font-family:'Cinzel',serif;font-weight:700;display:flex;align-items:center;justify-content:center}
.hero-visual{left:430px;top:165px;width:620px;height:420px;border-radius:40% 30% 40% 50%;background:linear-gradient(135deg,#8b8f96,#cfd2d6 60%,#6a5e54);opacity:.9}
.dots{display:flex;gap:10px}
.dots span{width:8px;height:8px;border-radius:50%;border:1.5px solid var(--navy)}

/* sections */
.ghost{font-family:'Cinzel',serif;font-weight:700;color:transparent;-webkit-text-stroke:1.5px var(--ghost);text-align:center;letter-spacing:2px}
.sec-title{font-family:'Cinzel',serif;font-weight:600;color:#111;text-align:center}
.sec-sub{text-align:center;font-size:12.5px;line-height:20px}
.topic h3{font-family:'Cinzel',serif;font-weight:700;color:var(--ink);font-size:24px;margin-bottom:12px}
.topic p{font-size:12.5px;line-height:19.5px}
.explore{display:inline-flex;align-items:center;gap:6px;margin-top:22px;color:var(--orange);font-family:'Cinzel',serif;font-weight:700;font-size:13px}
.explore i{width:11px;height:11px;border:1.5px solid var(--orange);border-radius:50%}
.illus{border-radius:50%}

/* team */
.team-card{left:161px;top:3008px;width:879px;height:355px;background:var(--white);box-shadow:0 0 10px rgba(0,0,0,.12);border-radius:4px;display:flex;padding:30px 16px 12px}
.member{flex:1;text-align:center;position:relative;padding:0 16px;height:100%}
.avatar{width:118px;height:118px;margin:0 auto;border-radius:50%;border:5px solid #eef0f2;background:radial-gradient(circle at 50% 40%,#666,#1c1c1c)}
.member h4{font-family:'Cinzel',serif;font-weight:700;color:#222;font-size:14px;margin-top:22px}
.member .role{color:#3a6fa8;font-size:11px;margin:4px 0 8px}
.member p{font-size:11.5px;line-height:19px}
.member .wave{position:absolute;left:2px;right:2px;bottom:0;width:calc(100% - 4px);height:50px}

/* news */
.news-head{font-family:'Cinzel',serif;font-weight:700;color:#222;font-size:14.5px;line-height:24px;text-align:center}
.arrow-c{width:30px;height:30px;border-radius:50%;border:1.5px solid var(--orange);display:flex;align-items:center;justify-content:center}
.thumb{border-radius:50%;background:linear-gradient(135deg,#4a4a4a,#1e1e1e)}

/* footer */
.foot-nav{display:flex;gap:22px;color:var(--white);font-size:12.5px}
.col h5{font-family:'Cinzel',serif;font-weight:700;color:var(--orange);font-size:13px;margin-bottom:20px}
.col li{list-style:none;color:var(--white);font-size:12px;line-height:24px}
.contact-row{display:flex;align-items:center;gap:14px;color:var(--white);font-size:12px;line-height:18px;margin-bottom:18px}
.ic{width:34px;height:34px;border:1.5px solid var(--white);border-radius:50%;display:flex;align-items:center;justify-content:center;flex:none}
.social{display:flex;gap:14px}
.social span{width:40px;height:40px;border:1.5px solid var(--white);border-radius:50%}
</style>
</head>
<body>

<!-- HERO -->
<section class="abs hero">
  <svg class="abs" style="left:0;top:0" width="1200" height="673" viewBox="0 0 1200 673">
    <circle cx="860" cy="330" r="200" fill="#27598a" opacity=".55"/>
    <path d="M1200 120 C1130 140 1110 200 1120 260 C1130 330 1050 350 1000 420 C950 490 990 560 1080 600 C1140 625 1180 620 1200 610 Z" fill="#2a6677"/>
    <path d="M1200 60 C1150 80 1120 130 1105 190 C1090 260 1080 300 1020 360" fill="none" stroke="#fff" stroke-width="14"/>
    <path d="M0 673 L380 673 C420 630 500 610 560 640 C620 665 700 640 800 600 C900 560 1000 610 1080 640 C1140 660 1180 640 1200 620 L1200 673 Z" fill="#fff"/>
  </svg>
  <div class="abs brand" style="left:160px;top:26px"><span class="brand-dot"></span>Northvale</div>
  <nav class="abs nav" style="left:545px;top:37px">
    <a>Home</a><a>About Us</a><a>Strategy</a><a>Investors</a><a>Team</a><a>News</a><a>Contact Us</a>
  </nav>
  <div class="abs phone-btn" style="left:1001px;top:27px">
    <svg width="18" height="18" viewBox="0 0 24 24"><path d="M6.6 10.8a15 15 0 0 0 6.6 6.6l2.2-2.2c.3-.3.7-.4 1-.2 1.1.4 2.3.6 3.6.6.6 0 1 .4 1 1V20c0 .6-.4 1-1 1A17 17 0 0 1 3 4c0-.6.4-1 1-1h3.5c.6 0 1 .4 1 1 0 1.3.2 2.5.6 3.6.1.3 0 .7-.2 1z" fill="#fff"/></svg>
  </div>
  <div class="abs hero-visual" role="img" aria-label="Laptop showing a team meeting around a table"></div>
  <h1 class="abs hero-title serif" style="left:162px;top:205px;width:620px">We Provide Flexible Capital To Innovative Companies And Their Investors</h1>
  <a class="abs btn" style="left:162px;top:428px;width:148px;height:50px;font-size:17px">Login Now</a>
  <div class="abs dots" style="left:485px;top:654px"><span></span><span></span><span></span></div>
</section>

<!-- STRATEGY -->
<div class="abs ghost" style="left:0;width:1200px;top:724px;font-size:80px">STRATEGY</div>
<h2 class="abs sec-title" style="left:0;width:1200px;top:768px;font-size:38px">Our Strategy</h2>
<p class="abs sec-sub" style="left:385px;width:430px;top:822px">Our focus spans the life science and technology industries, two sectors where intellectual property (IP) is an integral driver of asset and enterprise value.</p>

<div class="abs illus" style="left:740px;top:875px;width:500px;height:490px;background:linear-gradient(180deg,#6f9aa3,#e9eff1 85%,#fff)"></div>
<div class="abs" role="img" aria-label="Illustration of two scientists with microscope and lab equipment" style="left:577px;top:960px;width:515px;height:345px;background:linear-gradient(180deg,rgba(31,53,86,.25),rgba(63,107,170,.35));border-radius:8px"></div>
<div class="abs topic" style="left:162px;top:1017px;width:265px">
  <h3>Life Science</h3>
  <p>We have a long track record of partnering with companies and investors that create and commercialize life science products, with extensive experience spanning biopharmaceuticals, medical devices, and tools &amp; diagnostics.</p>
  <a class="explore">Explore More <i></i></a>
</div>

<div class="abs illus" role="img" aria-label="Illustration of a woman working with large data dashboards" style="left:-120px;top:1310px;width:640px;height:560px;background:radial-gradient(circle at 50% 40%,#ff8a5c,#ffc2a6 55%,#fff 78%)"></div>
<div class="abs topic" style="left:770px;top:1457px;width:268px;text-align:right">
  <h3>Technology</h3>
  <p>We uniquely offer sizeable and flexible structured credit financing solutions to innovative technology companies, with a focus on enterprise software, data &amp; analytics, semiconductors, and communications systems.</p>
  <a class="explore">Explore More <i></i></a>
</div>

<div class="abs illus" style="left:745px;top:1738px;width:520px;height:520px;background:linear-gradient(180deg,#5d7898,#dfe6ee 80%,#fff)"></div>
<div class="abs" role="img" aria-label="Illustration of businessmen with stacks of money, coins and bar charts" style="left:620px;top:1810px;width:470px;height:380px;background:linear-gradient(135deg,rgba(110,140,70,.35),rgba(240,190,40,.3),rgba(40,60,90,.3));border-radius:8px"></div>
<div class="abs topic" style="left:162px;top:1895px;width:265px">
  <h3>Transaction Type</h3>
  <p>Our proven strategy focuses on identifying opportunities where demonstrated commercial success has established underlying asset or enterprise value prior to our investment. We tailor our financing solutions to each situation with the goal of preserving.</p>
  <a class="explore">Explore More <i></i></a>
</div>

<!-- ABOUT -->
<svg class="abs" style="left:0;top:2250px" width="1200" height="565" viewBox="0 0 1200 565">
  <defs><linearGradient id="aboutGrad" x1="0" y1="0" x2="1" y2="0"><stop offset="0" stop-color="#224d72"/><stop offset="1" stop-color="#2a6677"/></linearGradient></defs>
  <path d="M0 110 C80 90 160 110 260 160 C360 210 480 120 600 80 C720 40 820 90 920 70 C1020 50 1080 30 1100 60 C1120 90 1160 70 1200 55 L1200 565 L0 565 Z" fill="url(#aboutGrad)"/>
  <path d="M260 60 C330 40 520 40 560 70 C580 100 420 120 320 120 C250 120 220 80 260 60 Z" fill="#224d72"/>
  <path d="M1080 20 C1110 -5 1160 10 1150 40 C1140 70 1090 60 1080 20 Z" fill="#224d72"/>
</svg>
<div class="abs" role="img" aria-label="Photo of a businessman at a desk looking at his phone" style="left:-10px;top:2446px;width:500px;height:500px;border-radius:50%;background:linear-gradient(135deg,#d8d2c8,#a99c8a 50%,#6f6353)"></div>
<div class="abs" style="left:0;top:2813px;width:1200px;height:140px;background:#fff"></div>
<div class="abs ghost" style="left:610px;top:2432px;font-size:62px;-webkit-text-stroke-color:rgba(255,255,255,.25);text-align:left">OUR INFO</div>
<h2 class="abs" style="left:612px;top:2468px;font-family:'Cinzel',serif;font-variant:small-caps;font-weight:600;color:#fff;font-size:40px">About Us</h2>
<div class="abs" style="left:612px;top:2530px;width:420px;color:#fff;font-size:12.5px;line-height:19.5px">
  <p>Northvale is a private investment firm unique in its dual focus on life science and technology credit opportunities. Our ambidextrous approach to investing reflects a broad recognition and appreciation for the critical role intellectual property plays in the successful commercialization of products.</p>
  <p style="margin-top:18px">We apply our extensive industry expertise to assess the revenue visibility created by these assets and offer a range of creative financing solutions.</p>
</div>
<a class="abs btn" style="left:611px;top:2704px;width:119px;height:36px;font-size:13px">Read More</a>

<!-- TEAM -->
<div class="abs ghost" style="left:0;width:1200px;top:2858px;font-size:76px">TEAM</div>
<h2 class="abs sec-title" style="left:0;width:1200px;top:2900px;font-size:38px">Our Team</h2>
<p class="abs sec-sub" style="left:380px;width:440px;top:2952px">We bring over 40 years of collective experience to our investments, including over $1.2B invested within structured credit, milestones and royalties.</p>
<div class="abs team-card">
  <div class="member">
    <div class="avatar" role="img" aria-label="Portrait of Marek Halloway"></div>
    <h4>Marek Halloway</h4>
    <div class="role">Managing Partner</div>
    <p>Marek Halloway is an industry leader with over $1.2B in structured credit investments since 2004.</p>
    <svg class="wave" viewBox="0 0 272 50" preserveAspectRatio="none"><path d="M0 0 C60 5 120 40 180 30 C220 22 250 20 272 25 L272 50 L0 50 Z" fill="#24566f"/></svg>
  </div>
  <div class="member">
    <div class="avatar" role="img" aria-label="Portrait of Samir Okonkwo"></div>
    <h4>Samir Okonkwo</h4>
    <div class="role">Managing Partner</div>
    <p>Samir Okonkwo leads technology investment origination and evaluation at Northvale. He has over 15 years of technology .</p>
    <svg class="wave" viewBox="0 0 272 50" preserveAspectRatio="none"><path d="M0 20 C70 10 150 15 272 45 L272 50 L0 50 Z" fill="#8da3b3"/><path d="M0 35 C90 25 180 30 272 48 L272 50 L0 50 Z" fill="#24566f"/></svg>
  </div>
  <div class="member">
    <div class="avatar" role="img" aria-label="Portrait of Tobias Renner"></div>
    <h4>Tobias Renner</h4>
    <div class="role">Partner</div>
    <p>Tobias Renner serves as the Chief Operating Officer at Northvale. He has 20 years of experience in the alternative.</p>
    <svg class="wave" viewBox="0 0 272 50" preserveAspectRatio="none"><path d="M0 0 L272 0 L272 50 L0 50 Z" fill="#e3ecee"/><path d="M30 50 C80 20 150 10 220 40 L230 50 Z" fill="#24566f"/></svg>
  </div>
</div>

<!-- NEWS + FOOTER BACKGROUND -->
<svg class="abs" style="left:0;top:3340px" width="1200" height="1161" viewBox="0 0 1200 1161">
  <defs><linearGradient id="footGrad" x1="0" y1="0" x2="1" y2="0"><stop offset="0" stop-color="#1e4a74"/><stop offset="1" stop-color="#2a6677"/></linearGradient></defs>
  <path d="M1200 50 C1160 60 1150 120 1160 200 C1175 300 1130 380 1080 450 C1020 530 1060 590 1100 620 L1200 620 Z" fill="#2a6677"/>
  <path d="M0 560 C30 590 30 640 0 680 Z" fill="#1e4a74"/>
  <path d="M0 700 C120 660 260 700 330 640 C400 580 520 600 560 650 C620 700 760 690 900 660 C1020 630 1100 600 1200 560 L1200 1161 L0 1161 Z" fill="url(#footGrad)"/>
</svg>

<div class="abs ghost" style="left:0;width:1200px;top:3420px;font-size:78px">INSIGHTS</div>
<h2 class="abs sec-title" style="left:0;width:1200px;top:3468px;font-size:38px">Latest News</h2>
<p class="abs sec-sub" style="left:390px;width:420px;top:3520px">A pioneer in providing life science structured credit beginning in 2004, the Northvale team was the first to introduce flexible.</p>
<h3 class="abs news-head serif" style="left:360px;width:480px;top:3590px">Northvale completes structured debt investment<br>in LumenPath</h3>
<div class="abs" style="left:0;width:1200px;top:3645px;text-align:center;color:#3a6fa8;font-size:11.5px">20 November 2019</div>
<p class="abs sec-sub" style="left:390px;width:420px;top:3668px;line-height:19.5px">Northvale Investment Partners ("Northvale") announced today that it has completed a structured debt investment in LumenPath, Inc. ("LumenPath"), the leader in employee communication. The financing will be used to advance LumenPath's continued growth as the SaaS company scales its market-leading Engage Suite software. LumenPath is headquartered in Harbor Point, California.</p>

<div class="abs arrow-c" style="left:257px;top:3848px"><svg width="10" height="12" viewBox="0 0 10 12"><path d="M7 1 L2 6 L7 11" fill="none" stroke="#f2693a" stroke-width="1.8"/></svg></div>
<div class="abs arrow-c" style="left:915px;top:3848px"><svg width="10" height="12" viewBox="0 0 10 12"><path d="M3 1 L8 6 L3 11" fill="none" stroke="#f2693a" stroke-width="1.8"/></svg></div>
<div class="abs thumb" role="img" aria-label="News thumbnail photo" style="left:346px;top:3830px;width:68px;height:68px"></div>
<div class="abs thumb" role="img" aria-label="News thumbnail photo" style="left:450px;top:3830px;width:68px;height:68px;background:linear-gradient(135deg,#777,#333)"></div>
<div class="abs thumb" role="img" aria-label="Featured news photo of a smiling businesswoman" style="left:552px;top:3815px;width:98px;height:98px;background:linear-gradient(135deg,#e9e3da,#b9ab98)"></div>
<div class="abs thumb" role="img" aria-label="News thumbnail photo" style="left:684px;top:3830px;width:68px;height:68px"></div>
<div class="abs thumb" role="img" aria-label="News thumbnail photo" style="left:788px;top:3830px;width:68px;height:68px;background:linear-gradient(135deg,#5a5a5a,#222)"></div>

<!-- FOOTER -->
<footer>
  <div class="abs" style="left:0;width:1200px;top:4072px;display:flex;justify-content:center">
    <div style="display:flex;align-items:center;gap:16px;color:#fff">
      <span style="width:42px;height:42px;border-radius:50%;background:#fff"></span>
      <div>
        <div style="font-family:'Cinzel',serif;font-weight:700;font-size:40px;line-height:42px">Northvale</div>
        <div style="font-family:'Cinzel',serif;font-weight:700;font-size:11px;letter-spacing:1px;margin-left:24px">INVESTMENT PARTNERS, LLC</div>
      </div>
    </div>
  </div>
  <nav class="abs foot-nav" style="left:385px;top:4170px">
    <a>Home</a><a>About Us</a><a>Strategy</a><a>Investors</a><a>Team</a><a>News</a><a>Contact Us</a>
  </nav>
  <div class="abs col" style="left:162px;top:4234px">
    <h5>Life Sciences</h5>
    <ul><li>Biopharma</li><li>Devices</li><li>Tools &amp; Diagnostics</li></ul>
  </div>
  <div class="abs col" style="left:387px;top:4234px">
    <h5>Technology</h5>
    <ul><li>Software &amp; Services</li><li>Hardware</li><li>Systems</li></ul>
  </div>
  <div class="abs col" style="left:613px;top:4234px">
    <h5>Transaction Type</h5>
    <ul><li>Structured Credit</li><li>Milestones &amp; Royalties</li><li>Legacy Assets</li></ul>
  </div>
  <div class="abs col" style="left:838px;top:4234px;width:220px">
    <h5>Contact Info</h5>
    <div class="contact-row"><span class="ic"><svg width="16" height="16" viewBox="0 0 24 24"><path d="M6.6 10.8a15 15 0 0 0 6.6 6.6l2.2-2.2c.3-.3.7-.4 1-.2 1.1.4 2.3.6 3.6.6.6 0 1 .4 1 1V20c0 .6-.4 1-1 1A17 17 0 0 1 3 4c0-.6.4-1 1-1h3.5c.6 0 1 .4 1 1 0 1.3.2 2.5.6 3.6.1.3 0 .7-.2 1z" fill="#fff"/></svg></span>+1-555-014-2290</div>
    <div class="contact-row"><span class="ic"><svg width="16" height="12" viewBox="0 0 16 12"><rect x="1" y="1" width="14" height="10" fill="none" stroke="#fff" stroke-width="1.5"/><path d="M1 1 L8 7 L15 1" fill="none" stroke="#fff" stroke-width="1.5"/></svg></span>inquiries@northvaleloan.com</div>
    <div class="contact-row"><span class="ic"><svg width="14" height="18" viewBox="0 0 14 18"><path d="M7 1 C3.5 1 1 3.6 1 7 C1 11 7 17 7 17 C7 17 13 11 13 7 C13 3.6 10.5 1 7 1 Z" fill="#fff"/><circle cx="7" cy="7" r="2.2" fill="#1e4a74"/></svg></span>420 Larkspur Avenue #210<br>Fairhaven, CA 90210</div>
  </div>
  <div class="abs social" style="left:162px;top:4363px"><span></span><span></span><span></span><span></span></div>
  <div class="abs" style="left:162px;top:4446px;width:876px;height:1px;background:rgba(255,255,255,.3)"></div>
  <div class="abs" style="left:0;width:1200px;top:4466px;text-align:center;color:#fff;font-size:11px">Copyrights © 2019 Northvale. All Rights Reserved, Terms &amp; Conditions | Privacy Policy.</div>
</footer>

</body>
</html>
```